Velduna.com webside

I want to build a Velduna.com retail website use on Shopify, reselling three main categories: Office Supplies, Packing Supplies, and Home Consumables. I also wish the webpage has the same functions as the Corvelt home page. The page is split into three different parts with the top being a sliding screen showcasing promotion products, below it being the three categories, and finally, a moving screen showing company missions.
Target Market(s)
U.S online
Industry/Entity Type
Office Supplies, packing Supplies and Home Consumables
Coding
Coded - Design and coding required
Number of Pages Required
5+ page
Look and feel

```html
<!DOCTYPE html>
<html lang="en">
<head>
<meta charset="UTF-8">
<title>Velduna – Office Supplies</title>
<link rel="stylesheet" href="https://fonts.googleapis.com/css2?family=Montserrat:wght@400;500;700;800&family=Roboto:wght@400&display=swap">
<style>
  :root {
    --brand: #00a98b;
    --brand-tint: #e8f8f4;
    --ink: #111111;
    --white: #ffffff;
    --photo-light: #f1ece4;
    --photo-mid: #d9c7a6;
  }
  * { box-sizing: border-box; margin: 0; padding: 0; }
  html, body { width: 1200px; height: 550px; overflow: hidden; background: var(--white); }
  body { font-family: "Montserrat", sans-serif; color: var(--ink); position: relative; }

  .promo-bar {
    height: 50px; background: var(--brand-tint);
    display: flex; align-items: center; justify-content: space-between;
    padding: 0 118px 0 108px; font-size: 15px;
  }
  .account { display: flex; align-items: center; gap: 8px; }
  .account-login { display: flex; align-items: center; gap: 8px; padding-right: 8px; border-right: 1px solid var(--ink); height: 24px; }
  .currency { display: flex; align-items: center; gap: 6px; }

  .main-nav {
    height: 83px; background: var(--brand);
    display: flex; align-items: center; padding: 0 110px 0 108px; color: var(--white);
  }
  .brand-name { font-weight: 800; font-size: 31px; letter-spacing: 0.3px; width: 250px; }
  .nav-links { display: flex; gap: 33px; list-style: none; font-size: 15px; }
  .nav-links li { position: relative; padding: 4px 0; }
  .nav-links .is-active { font-weight: 700; }
  .nav-links .is-active::after {
    content: ""; position: absolute; left: 0; right: 0; bottom: -5px; height: 3px; background: var(--white);
  }
  .nav-tools { margin-left: auto; display: flex; gap: 16px; align-items: center; }

  .hero { position: relative; height: 417px; }
  .hero-visual {
    position: absolute; left: 667px; top: 17px; width: 533px; height: 400px;
    background: radial-gradient(ellipse at 45% 45%, var(--photo-light) 0%, var(--white) 60%),
                linear-gradient(160deg, var(--white) 45%, var(--photo-mid) 100%);
  }
  .hero-copy { position: absolute; left: 108px; top: 118px; z-index: 1; }
  .hero-title {
    font-weight: 700; font-size: 45px; line-height: 1.1; color: var(--brand);
    white-space: nowrap;
  }
  .hero-subtitle { font-family: "Roboto", sans-serif; font-size: 19px; margin: 20px 0 0 3px; }
  .hero-cta {
    display: inline-flex; align-items: center; justify-content: center;
    margin-top: 34px; width: 150px; height: 50px;
    border: 2px solid var(--brand); color: var(--brand); font-size: 16px; font-weight: 500;
    text-decoration: none;
  }
  .slider-arrow { position: absolute; top: 192px; z-index: 1; }
  .slider-arrow.prev { left: 48px; }
  .slider-arrow.next { left: 1128px; }
</style>
</head>
<body>
  <div class="promo-bar">
    <span>New Year Sale - 30% off</span>
    <div class="account">
      <span class="account-login">
        <svg width="20" height="20" viewBox="0 0 20 20" aria-hidden="true"><circle cx="10" cy="10" r="10" fill="#111"/><circle cx="10" cy="8" r="3.3" fill="#e8f8f4"/><path d="M4.5 16a6.5 5 0 0 1 11 0" fill="#e8f8f4"/></svg>
        Login
      </span>
      <span class="currency">$USD
        <svg width="16" height="10" viewBox="0 0 16 10" aria-hidden="true"><path d="M1 1l7 7 7-7" fill="none" stroke="#111" stroke-width="2"/></svg>
      </span>
    </div>
  </div>

  <nav class="main-nav">
    <div class="brand-name">Velduna</div>
    <ul class="nav-links">
      <li class="is-active">Home</li>
      <li>Categories</li>
      <li>Products</li>
      <li>Blog</li>
      <li>Shop</li>
      <li>Contact</li>
    </ul>
    <div class="nav-tools">
      <svg width="22" height="22" viewBox="0 0 22 22" aria-label="Search"><circle cx="9.5" cy="9.5" r="7.5" fill="none" stroke="#fff" stroke-width="2.2"/><path d="M15 15l5.5 5.5" stroke="#fff" stroke-width="2.2" stroke-linecap="round"/></svg>
      <svg width="25" height="22" viewBox="0 0 25 22" aria-label="Wishlist"><path d="M12.5 20S2 13.5 2 7a5 5 0 0 1 10.5-2 5 5 0 0 1 10.5 2c0 6.5-10.5 13-10.5 13z" fill="none" stroke="#fff" stroke-width="2"/></svg>
      <svg width="20" height="22" viewBox="0 0 20 22" aria-label="Cart"><rect x="2" y="7" width="16" height="13" rx="1.5" fill="none" stroke="#fff" stroke-width="2"/><path d="M6 9V5a4 4 0 0 1 8 0v4" fill="none" stroke="#fff" stroke-width="2"/></svg>
    </div>
  </nav>

  <section class="hero">
    <div class="hero-visual" role="img" aria-label="Coloured pencils in a wire mesh holder with notebooks, paper clips, push pins and a sharpener"></div>
    <svg class="slider-arrow prev" width="22" height="34" viewBox="0 0 22 34" aria-label="Previous slide"><path d="M18 2L4 17l14 15" fill="none" stroke="#111" stroke-width="2.6"/></svg>
    <div class="hero-copy">
      <h1 class="hero-title">1 set of office supplies</h1>
      <p class="hero-subtitle">Get the complete product now</p>
      <a class="hero-cta" href="#">Order Now</a>
    </div>
    <svg class="slider-arrow next" width="22" height="34" viewBox="0 0 22 34" aria-label="Next slide"><path d="M4 2l14 15L4 32" fill="none" stroke="#111" stroke-width="2.6"/></svg>
  </section>
</body>
</html>
```